Nine nights by a quiet lake - II

Cover for the book "Nine nights by the side of a lake".
Author: "Corinne Malvaux"
Publisher: "Editions Pervanche" (at the bottom of the page)
Book 14 x 20.5 cm

In the previous project ("9 nights by a quiet lake"), I proposed a photo of a woman with silvery hair.
I think I made a mistake that forced the artists in a direction and limited the creativity.

Therefore, I now offer only key-words:
A mature woman, still beautiful and dressed like a young one, also sensual and radiant.
She is on vacation by the seaside.

Please note that the cover is in French:
Corinne Malvaux
Nine nights by a quiet lake
Pervanche Editions

Target Market(s)

Adults, all ages, often women

Industry/Entity Type

book

Requirements
Must have
• elegance, maybe a bit of snobbery

```html
<!DOCTYPE html>
<html lang="fr">
<head>
<meta charset="utf-8">
<title>Neuf nuits au bord d'un lac — Corinne Malvaux</title>
<link rel="stylesheet" href="https://fonts.googleapis.com/css2?family=EB+Garamond:wght@400&family=Questrial&family=Montserrat:wght@600&display=swap">
<style>
  :root {
    --sky-top: #d4d1e6;
    --sky-mid: #e7bdd0;
    --sky-glow: #f1a896;
    --horizon: #9c7ea6;
    --sea-deep: #4f5598;
    --sea-foam: #8f93c8;
    --sand: #a58cb4;
    --sand-low: #8878a8;
    --author-ink: #5b5a7d;
    --title-ink: #ffffff;
    --band: #8884aa;
    --band-ink: #ffffff;
  }
  * { margin: 0; padding: 0; box-sizing: border-box; }
  html, body { width: 857px; height: 1200px; overflow: hidden; background: #ffffff; }
  .cover {
    position: relative;
    width: 857px;
    height: 1200px;
    overflow: hidden;
  }
  .cover__photo {
    position: absolute;
    inset: 0 0 95px 0;
    background: linear-gradient(180deg,
      var(--sky-top) 0%,
      var(--sky-mid) 18%,
      var(--sky-glow) 36%,
      #d99aa6 43%,
      var(--horizon) 47%,
      var(--sea-deep) 50%,
      var(--sea-foam) 55%,
      var(--sea-deep) 59%,
      var(--sea-foam) 63%,
      var(--sand) 70%,
      #b89ab8 82%,
      var(--sand-low) 100%);
  }
  .cover__author {
    position: absolute;
    top: 50px;
    left: 0;
    width: 100%;
    text-align: center;
    font-family: "Questrial", sans-serif;
    font-size: 46px;
    letter-spacing: 0.3em;
    text-indent: 0.3em;
    color: var(--author-ink);
    line-height: 1;
  }
  .cover__title {
    font-family: "EB Garamond", serif;
    font-weight: 400;
    color: var(--title-ink);
    line-height: 1;
  }
  .title-line {
    position: absolute;
    white-space: nowrap;
    display: block;
  }
  .title-line--lead {
    top: 168px;
    left: 0;
    width: 857px;
    text-align: center;
    font-size: 96px;
    letter-spacing: 0.12em;
    text-indent: 0.12em;
  }
  .title-line--small-right {
    top: 308px;
    right: 78px;
    font-size: 76px;
    letter-spacing: 0.14em;
    margin-right: -0.14em;
  }
  .title-line--big-right {
    top: 420px;
    right: 60px;
    font-size: 150px;
    letter-spacing: 0.1em;
    margin-right: -0.1em;
  }
  .title-line--small-mid {
    top: 793px;
    left: 300px;
    font-size: 72px;
    letter-spacing: 0.14em;
  }
  .title-line--big-wide {
    top: 870px;
    left: 0;
    width: 857px;
    text-align: center;
    font-size: 150px;
    letter-spacing: 0.3em;
    text-indent: 0.3em;
  }
  .cover__publisher {
    position: absolute;
    left: 0;
    bottom: 0;
    width: 100%;
    height: 95px;
    background: var(--band);
    display: flex;
    align-items: center;
    justify-content: center;
  }
  .publisher-name {
    font-family: "Montserrat", sans-serif;
    font-weight: 600;
    font-size: 21px;
    letter-spacing: 0.14em;
    margin-right: -0.14em;
    color: var(--band-ink);
  }
</style>
</head>
<body>
  <main class="cover">
    <div class="cover__photo" role="img" aria-label="Photographie : une femme de dos, cheveux au vent, marchant pieds nus au bord de l'eau au coucher du soleil, ciel rose et lavande, vagues bleutées"></div>
    <p class="cover__author">CORINNE MALVAUX</p>
    <h1 class="cover__title">
      <span class="title-line title-line--lead">NEUF NUITS</span>
      <span class="title-line title-line--small-right">AU</span>
      <span class="title-line title-line--big-right">BORD</span>
      <span class="title-line title-line--small-mid">D’UN</span>
      <span class="title-line title-line--big-wide">LAC</span>
    </h1>
    <footer class="cover__publisher">
      <span class="publisher-name">EDITIONS PERVANCHE</span>
    </footer>
  </main>
</body>
</html>
```